NOVETHA - Bridging Science and Discovery toward Equal Opportunity

Brochure is needed for the European Project "NOVETHA". We will distribute this flyer during conferences and events to our audiences (mainly academics, researchers, business individuals, policy makers and members of civil society groups) in order to provide the basic information about the project.
The main scope of the project is to support research organisations across Europe to design and implement gender equality plans in order to promote the women’s position of the filed of STEM research.

We are providing a video to explain the layout: https://www.vidmorel.com/watch?v=Tb8KpZ2_RwX.
We think size can range from A4-A3.

We are attaching files to provide with concrete information on our requirements:
- NOVETHA Brochure Layout_SA.ppt: includes the content we would like to include in the flyer. There is also the URL to the project website
- novetha Logo.zip: the project logo
- Partners Logos.zip: the Logos that will be included
We would like to use colours that belong to the project logo colour range. Regarding the images that you may include in the flyer, we wouldn't like to propose any because we do not want to limitate your imagination. We have some at the website https://novetha-project.eu/. They could be diverse (age, race, gender, etc.) relevant to women and men.

```html
<!DOCTYPE html>
<html lang="en">
<head>
<meta charset="utf-8">
<title>NOVETHA Brochure</title>
<link rel="stylesheet" href="https://fonts.googleapis.com/css2?family=Montserrat:wght@500;600;700;800&family=Open+Sans:wght@400;600;700&display=swap">
<style>
:root{
  --purple:#4a3a96;
  --purple-dark:#3a2d7c;
  --yellow:#f6b91c;
  --white:#ffffff;
  --ink:#333344;
  --muted:#6d6d7a;
  --stage:#e9e9ec;
  --photo-a:#8797ad;
  --photo-b:#d5d9df;
  --photo-c:#5e6779;
}
*{box-sizing:border-box;margin:0;padding:0}
html,body{width:1200px;height:3000px;overflow:hidden}
body{background:var(--stage);font-family:"Open Sans",Arial,sans-serif;color:var(--ink);position:relative}
.spread{position:absolute;left:60px;width:1080px;height:764px;display:flex;box-shadow:0 6px 24px rgba(0,0,0,.15)}
.spread--outer{top:80px}
.spread--inner{top:904px}
.page{position:relative;width:540px;height:764px;overflow:hidden;background:var(--white)}
.page + .page{border-left:1px solid rgba(0,0,0,.08)}
.page svg.shapes{position:absolute;inset:0;width:100%;height:100%}
.abs{position:absolute}
.heading{font-family:"Montserrat",Arial,sans-serif;font-weight:800;text-transform:uppercase;color:var(--yellow);letter-spacing:.3px}
.photo{position:absolute;background:linear-gradient(135deg,var(--photo-a),var(--photo-b) 45%,var(--photo-c))}
.photo--oval{border-radius:50%}
.arc{position:absolute;border-radius:50%;background:var(--yellow)}

/* brand lockup */
.brand{position:absolute;text-align:center;left:0;right:0}
.brand__mark{display:inline-block;width:26px;height:26px;border-radius:50%;background:var(--yellow);vertical-align:middle;margin-right:10px}
.brand__name{font-family:"Montserrat",Arial,sans-serif;font-weight:600;color:var(--purple);vertical-align:middle}
.brand__sub{font-size:11px;color:var(--purple);margin-top:2px}

/* cover */
.cover__brand{top:60px}
.cover__brand .brand__name{font-size:42px;letter-spacing:2px}
.cover__title{left:40px;right:40px;top:600px;text-align:center;color:var(--white);font-family:"Montserrat",Arial,sans-serif;font-weight:700;font-size:19px;line-height:1.3;text-transform:uppercase}
.cover__rule{left:255px;top:668px;width:30px;height:2px;background:var(--yellow)}
.cover__funding{left:40px;right:40px;top:684px;text-align:center;color:#dcd8f0;font-size:8px;line-height:1.4}

/* back */
.back__halo{left:70px;top:70px;width:220px;height:220px;border-radius:50%;border:26px solid #f0f0f2}
.back__brand{top:170px}
.back__brand .brand__mark{width:18px;height:18px;margin-right:8px}
.back__brand .brand__name{font-size:30px;letter-spacing:1.5px}
.back__brand .brand__sub{font-size:9px}
.back__tagline{left:0;right:0;top:250px;text-align:center;font-size:12px;color:var(--muted)}
.back__panel{left:0;right:0;top:440px;bottom:0;background:var(--purple);color:var(--white);text-align:center;padding:50px 50px 0}
.back__panel .heading{font-size:18px;margin-bottom:16px}
.back__panel p{font-size:11px;line-height:1.55}
.back__url{font-family:"Montserrat",Arial,sans-serif;font-weight:700;letter-spacing:2px;font-size:13px;margin:10px 0 36px}
.social{display:flex;justify-content:center;gap:20px;margin-top:14px;font-size:9px}
.social span::before{content:"";display:inline-block;width:9px;height:9px;background:var(--yellow);margin-right:5px;vertical-align:-1px}

/* inner left */
.band{left:0;right:0;top:0;height:228px;background:var(--purple);color:var(--white);padding:34px 36px 0}
.band .heading{font-size:16px;line-height:1.2;margin-bottom:10px}
.band p{font-size:9.5px;line-height:1.5;color:#e3e0f4}
.stakeholders{display:grid;grid-template-columns:1fr 1fr;gap:3px 18px;margin:8px 0 10px;font-size:9px;font-weight:700;list-style:none}
.stakeholders li::before{content:"";display:inline-block;width:5px;height:5px;border-radius:50%;background:var(--yellow);margin-right:7px;vertical-align:1px}
.impact-tab{left:0;top:228px;width:220px;height:28px;background:var(--yellow);padding:6px 36px;font-family:"Montserrat",Arial,sans-serif;font-weight:800;font-size:13px;color:var(--white);clip-path:polygon(0 0,100% 0,92% 100%,0 100%)}
.impact-text{left:36px;right:36px;top:278px;font-size:9.5px;line-height:1.55;color:var(--ink)}
.people{left:28px;top:430px;width:200px;height:260px;border-radius:6px}
.aims{left:240px;top:420px;width:280px;background:var(--purple);color:var(--white);padding:16px 16px;list-style:none}
.aims li{display:flex;align-items:center;gap:12px;font-size:9px;font-weight:700;line-height:1.4;margin-bottom:14px}
.aims li:last-child{margin-bottom:0}
.aims__icon{flex:none;width:32px;height:32px;border-radius:50%;border:2px solid var(--white);display:flex;align-items:center;justify-content:center}
.footnote{left:262px;top:660px;font-size:8px;color:var(--ink);line-height:1.4}

/* inner right */
.band--consortium{height:200px}
.partners{left:40px;right:40px;top:250px;display:grid;grid-template-columns:repeat(3,1fr);gap:34px 26px}
.badge{height:52px;display:flex;align-items:center;justify-content:center}
.badge i{display:block;background:#d9d6e8}
.badge--wide i{width:110px;height:30px;border-radius:4px}
.badge--round i{width:50px;height:50px;border-radius:50%;background:#f2b79d}
.badge--square i{width:44px;height:44px;background:#c9c4df}
.badge--gold i{width:46px;height:50px;border-radius:50%;background:#e8d7a8}

/* goal page */
.goal{position:absolute;left:250px;top:1728px;width:700px;height:990px;background:var(--white);overflow:hidden;box-shadow:0 6px 24px rgba(0,0,0,.15)}
.goal svg.shapes{position:absolute;inset:0;width:100%;height:100%}
.goal__heading{left:40px;top:560px;font-size:16px}
.goal__text{left:40px;top:590px;width:400px;font-size:10.5px;line-height:1.55;color:var(--ink)}
.goal__text p + p{margin-top:10px}
.goal__scene{left:0;right:0;top:740px;height:210px;background:linear-gradient(120deg,#c9ccd3,#eef0f3 40%,#9aa2b2)}
.goal__url{right:26px;top:918px;color:var(--white);font-family:"Montserrat",Arial,sans-serif;font-weight:700;letter-spacing:3px;font-size:14px}
.goal__footer{left:0;right:0;top:950px;height:40px;background:var(--yellow);border-top:6px solid var(--purple)}
</style>
</head>
<body>

<!-- Outer spread: back + cover -->
<section class="spread spread--outer">
  <article class="page back">
    <div class="abs back__halo"></div>
    <div class="brand back__brand">
      <span class="brand__mark"></span><span class="brand__name">NOVETHA</span>
      <div class="brand__sub">Gender Equality in STEM Research</div>
    </div>
    <p class="abs back__tagline">Bridging Science and Discovery toward Equal Opportunity</p>
    <div class="abs back__panel">
      <h2 class="heading">Join NOVETHA</h2>
      <p>To learn more about NOVETHA, the Gender Equality Plans<br>and how to become part of the Research and Innovation Hubs of NOVETHA,<br>visit project's website at</p>
      <p class="back__url">www.novetha-project.eu</p>
      <p>Follow NOVETHA on social media platforms for the latest<br>updates on project actions</p>
      <div class="social"><span>Novetha EU</span><span>Novetha EU</span><span>@NovethaEU</span></div>
    </div>
  </article>

  <article class="page cover">
    <svg class="shapes" viewBox="0 0 540 764" aria-hidden="true">
      <path d="M0 470 C170 420 330 340 540 250 L540 764 L0 764 Z" fill="var(--purple)"/>
    </svg>
    <div class="brand cover__brand">
      <span class="brand__mark"></span><span class="brand__name">NOVETHA</span>
      <div class="brand__sub">Gender Equality in STEM Research</div>
    </div>
    <div class="arc" style="left:48px;top:188px;width:476px;height:350px;transform:rotate(-8deg)"></div>
    <div class="photo photo--oval" role="img" aria-label="Photo of a diverse team of researchers discussing around a table" style="left:40px;top:176px;width:470px;height:344px;transform:rotate(-8deg)"></div>
    <h1 class="abs cover__title">Bridging Science and Discovery<br>toward Equal Opportunity</h1>
    <div class="abs cover__rule"></div>
    <p class="abs cover__funding">This project has received funding from the Meridian Research Programme<br>under Grant Agreement No 800417</p>
  </article>
</section>

<!-- Inner spread: hubs + consortium -->
<section class="spread spread--inner">
  <article class="page hubs">
    <div class="abs band">
      <h2 class="heading">NOVETHA Research &amp;<br>Innovation Hubs</h2>
      <p>The RPOs/RFOs of the project establish local Research &amp; Innovation Hubs with the following stakeholders:</p>
      <ul class="stakeholders">
        <li>Academia and Universities</li><li>Government &amp; Public Sector</li>
        <li>Industry and Business</li><li>Civil society</li>
      </ul>
      <p>The strategic synergies stimulate dialogues to identify gaps and challenges related to gender inequalities at the different levels of the education-research-transfer to market and innovation chain.</p>
    </div>
    <div class="abs impact-tab">IMPACT</div>
    <p class="abs impact-text">NOVETHA vision is to enhance the gender balance in STEM fields and promote a greater engagement of female researchers with research and innovation, contributing to the ERA1 priorities on Gender Equality and stimulating a dialogue and collaboration between academia, public authorities, professionals and industry players in order to tackle gender inequalities across the research-transfer-to-market and innovation chain.</p>
    <div class="photo people" role="img" aria-label="Photo of a group of smiling professionals standing with arms crossed"></div>
    <ul class="abs aims">
      <li><span class="aims__icon"><svg width="16" height="16" viewBox="0 0 16 16"><path d="M3 8l3 3 7-7" stroke="#fff" stroke-width="2" fill="none"/></svg></span>Remove barriers to the recruitment, retention and career progression of female researchers</li>
      <li><span class="aims__icon"><svg width="16" height="16" viewBox="0 0 16 16"><path d="M3 8l3 3 7-7" stroke="#fff" stroke-width="2" fill="none"/></svg></span>Improve the gender balance in decision-making bodies</li>
      <li><span class="aims__icon"><svg width="16" height="16" viewBox="0 0 16 16"><path d="M3 8l3 3 7-7" stroke="#fff" stroke-width="2" fill="none"/></svg></span>Integrate the gender dimension in research and innovation content, improving the quality and societal relevance of produced knowledge, technologies and innovations.</li>
    </ul>
    <p class="abs footnote">1 Communication of the Research Council<br>of the 17.07.2017</p>
  </article>

  <article class="page consortium">
    <div class="abs band band--consortium">
      <h2 class="heading">Consortium</h2>
      <p>NOVETHA consists of 7 Research Performing Organisations (RPOs) and 2 Research Funding Organisations (RFOs) to develop a GEP covering a wide area around Europe, including 6 EU countries, Turkey and Georgia. The project also includes 2 SMEs undertaking project coordination (Vireo Labs) and the scientific management (Canale Works) and a professional association (Junior Scholars Forum) to expand the project results.</p>
    </div>
    <div class="abs partners">
      <div class="badge badge--wide"><i></i></div>
      <div class="badge badge--round"><i></i></div>
      <div class="badge badge--square"><i></i></div>
      <div class="badge badge--wide"><i></i></div>
      <div class="badge badge--wide"><i></i></div>
      <div class="badge badge--wide"><i></i></div>
      <div class="badge badge--square"><i></i></div>
      <div class="badge badge--square"><i></i></div>
      <div class="badge badge--wide"><i></i></div>
      <div class="badge badge--wide"><i></i></div>
      <div class="badge badge--square"><i></i></div>
      <div class="badge badge--gold"><i></i></div>
      <div class="badge badge--wide"><i></i></div>
    </div>
  </article>
</section>

<!-- Single page: the goal -->
<article class="goal">
  <svg class="shapes" viewBox="0 0 700 990" aria-hidden="true">
    <path d="M0 0 H700 V430 C500 480 260 510 0 540 Z" fill="var(--purple)"/>
  </svg>
  <div class="arc" style="left:86px;top:-36px;width:700px;height:520px;transform:rotate(-6deg)"></div>
  <div class="photo photo--oval" role="img" aria-label="Photo of a confident business team standing with arms crossed" style="left:80px;top:-58px;width:700px;height:514px;transform:rotate(-6deg)"></div>
  <h2 class="abs heading goal__heading">The Goal</h2>
  <div class="abs goal__text">
    <p>NOVETHA project supports 7 RPOs and 2 RFOs, that are in an initial stage, to develop Gender Equality Plans (GEPs) and engage the local Innovation Hubs to transfer the gained knowledge beyond academia.</p>
    <p>The project goal is to make research organisations more gender equal by increasing the number of female researchers in STEM, improving their careers prospects and integrating a gender dimension in research.</p>
  </div>
  <div class="abs goal__scene" role="img" aria-label="Photo of colleagues shaking hands across a meeting table"></div>
  <p class="abs goal__url">www.novetha-project.eu</p>
  <div class="abs goal__footer"></div>
</article>

</body>
</html>
```